Business Card cabinets and cabinets components making company.

the card should be formal and interesting at the same time. The main colors will be black and white.

Font styles to use
Sans Serif

Colors

Designer to choose only greyscale colors for use in the design.

Requirements
Must have
• At least must have the followings:
office phone
cell phone
address
position
name
email
web

```html
<!DOCTYPE html>
<html lang="en">
<head>
<meta charset="utf-8">
<title>Trimline Business Card</title>
<link rel="stylesheet" href="https://fonts.googleapis.com/css2?family=Montserrat:wght@400;600&family=Open+Sans:wght@400;700&display=swap">
<style>
  :root {
    --backdrop: #3a3a3a;
    --card-dark: #1f1f1f;
    --card-light: #f7f7f7;
    --ink-light: #ffffff;
    --ink-soft: #e6e6e6;
    --ink-dark: #222222;
  }
  * { margin: 0; padding: 0; box-sizing: border-box; }
  html, body {
    width: 1200px;
    height: 1200px;
    overflow: hidden;
    background: var(--backdrop);
  }
  .canvas {
    position: relative;
    width: 1200px;
    height: 1200px;
  }
  .card {
    position: absolute;
    left: 161px;
    width: 878px;
    height: 504px;
    box-shadow: 0 14px 30px rgba(0,0,0,0.45);
  }
  .card--front { top: 68px; background: var(--card-dark); color: var(--ink-light); }
  .card--back { top: 626px; background: var(--card-light); color: var(--ink-dark); }

  .brand {
    position: absolute;
    display: flex;
    align-items: center;
    font-family: "Montserrat", sans-serif;
    font-weight: 600;
    white-space: nowrap;
  }
  .brand__mark { display: block; }
  .card--front .brand {
    left: 217px; top: 250px;
    transform: translate(-50%, -50%);
    font-size: 52px;
    gap: 14px;
  }
  .card--front .brand__mark { width: 22px; height: 22px; background: var(--ink-light); }
  .card--back .brand {
    left: 439px; top: 202px;
    transform: translate(-50%, -50%);
    font-size: 112px;
    gap: 28px;
  }
  .card--back .brand__mark { width: 46px; height: 46px; background: var(--ink-dark); }

  .divider {
    position: absolute;
    left: 439px; top: 102px;
    width: 2px; height: 298px;
    background: var(--ink-soft);
  }
  .identity {
    position: absolute;
    left: 518px; top: 110px;
    font-family: "Open Sans", sans-serif;
  }
  .identity__name {
    font-weight: 700;
    font-size: 29px;
    letter-spacing: 2.5px;
  }
  .identity__role {
    font-size: 23px;
    letter-spacing: 1.5px;
    margin-top: 2px;
    color: var(--ink-soft);
  }
  .contacts {
    position: absolute;
    left: 518px; top: 222px;
    list-style: none;
    font-family: "Montserrat", sans-serif;
    font-size: 19px;
    letter-spacing: 0.6px;
  }
  .contacts__item {
    display: flex;
    align-items: center;
    height: 28px;
    margin-bottom: 10px;
  }
  .contacts__item--address { margin-top: 22px; }
  .contacts__icon { width: 46px; display: flex; align-items: center; }
  .contacts__icon svg { fill: var(--ink-light); }

  .website {
    position: absolute;
    left: 0; right: 0; top: 398px;
    text-align: center;
    font-family: "Open Sans", sans-serif;
    font-size: 25px;
    letter-spacing: 7px;
  }
</style>
</head>
<body>
<main class="canvas">
  <section class="card card--front">
    <div class="brand"><span class="brand__mark"></span><span class="brand__name">Trimline</span></div>
    <div class="divider"></div>
    <div class="identity">
      <p class="identity__name">YOUR NAME</p>
      <p class="identity__role">Position</p>
    </div>
    <ul class="contacts">
      <li class="contacts__item">
        <span class="contacts__icon"><svg width="14" height="20" viewBox="0 0 14 20"><path d="M2 0h10a2 2 0 0 1 2 2v16a2 2 0 0 1-2 2H2a2 2 0 0 1-2-2V2a2 2 0 0 1 2-2zm0 3v12h10V3zm5 13.2a1 1 0 1 0 0 2 1 1 0 0 0 0-2z"/></svg></span>
        <span>9876543021</span>
      </li>
      <li class="contacts__item">
        <span class="contacts__icon"><svg width="20" height="20" viewBox="0 0 24 24"><path d="M6.6 10.8a15.1 15.1 0 0 0 6.6 6.6l2.2-2.2a1 1 0 0 1 1-.25 11.4 11.4 0 0 0 3.6.57 1 1 0 0 1 1 1V20a1 1 0 0 1-1 1A17 17 0 0 1 3 4a1 1 0 0 1 1-1h3.5a1 1 0 0 1 1 1c0 1.25.2 2.45.57 3.6a1 1 0 0 1-.25 1z"/></svg></span>
        <span>0123456789</span>
      </li>
      <li class="contacts__item">
        <span class="contacts__icon"><svg width="20" height="15" viewBox="0 0 20 15"><path d="M0 0h20v2L10 8 0 2z"/><path d="M0 4l10 6 10-6v11H0z"/></svg></span>
        <span>youremail@mail.com</span>
      </li>
      <li class="contacts__item contacts__item--address">
        <span class="contacts__icon"><svg width="15" height="20" viewBox="0 0 15 20"><path d="M7.5 0A7.5 7.5 0 0 0 0 7.5C0 13 7.5 20 7.5 20S15 13 15 7.5A7.5 7.5 0 0 0 7.5 0zm0 10.5a3 3 0 1 1 0-6 3 3 0 0 1 0 6z"/></svg></span>
        <span>your business address</span>
      </li>
    </ul>
  </section>

  <section class="card card--back">
    <div class="brand"><span class="brand__mark"></span><span class="brand__name">Trimline</span></div>
    <p class="website">www.website.com</p>
  </section>
</main>
</body>
</html>
```